IT Consultancy Web Site

We need a twitter bootstrap, hero based designed for our IT Consultancy firm based in Adelaide, Australia called "Brenwick IT Consulting". We provide custom software development. We have some core areas of the site we wish to develop further at a later point. A blog, an ecommerce shop, and products / services listings - All three of these should have clearly visible navigation below the hero.

The final design should be clean and minimalist. It should communicate professionalism and elegance.

Industry/Entity Type

Shop

Requirements
Nice to have
• We currently do not have a logo, so inclusion of something simple in the design would be a bonus

```html
<!DOCTYPE html>
<html lang="en">
<head>
<meta charset="utf-8">
<title>Brenwick IT Consulting</title>
<link href="https://fonts.googleapis.com/css2?family=Arimo:wght@400;700&family=Questrial&family=Oswald:wght@300;500;700&display=swap" rel="stylesheet">
<style>
:root{
  --ink:#141414;
  --rule:#5a4436;
  --tan:#8a7668;
  --beige:#dccdbd;
  --cream:#f2e9df;
  --footer:#857164;
  --text:#2f2f2f;
  --muted:#555;
  --accent:#2a97d6;
  --brown:#6a4a35;
  --white:#fff;
  --hero-dark:#8f847d;
  --hero-light:#cdc3bb;
}
*{margin:0;padding:0;box-sizing:border-box}
html,body{width:923px;height:1200px;overflow:hidden}
body{position:relative;font-family:"Arimo",Arial,sans-serif;color:var(--text);
  background:linear-gradient(#eceae8 347px,#fff 380px,#fff 860px,#e9e7e5 920px)}
.abs{position:absolute}

.site-header{left:0;top:0;width:923px;height:67px;background:linear-gradient(#1e1e1e,#000);border-bottom:4px solid var(--rule)}
.brand{left:26px;top:18px;font-family:"Questrial",sans-serif;font-size:21px;color:#d9d9d9;letter-spacing:.5px;white-space:nowrap}
.main-nav{right:18px;top:0;display:flex}
.main-nav a{display:block;font-family:"Questrial",sans-serif;font-size:16px;color:#e8e8e8;text-decoration:none;padding:18px 11px 0;height:63px}
.main-nav a.active{border-top:2px solid var(--accent);padding-top:16px}

.hero{left:0;top:67px;width:923px;height:280px;
  background:linear-gradient(100deg,var(--hero-dark),var(--hero-light) 60%,var(--hero-dark))}

.feature{top:322px;width:211px;height:244px;text-align:center;
  background:linear-gradient(transparent 82px,var(--beige) 82px)}
.feature svg.cap{position:absolute;left:0;top:0}
.feature .badge{position:absolute;left:67px;top:43px;width:78px;height:78px;border-radius:50%;background:var(--ink);border:3px solid #7e6a5c;display:flex;align-items:center;justify-content:center}
.feature h3{position:absolute;top:130px;left:0;width:100%;font-family:"Questrial",sans-serif;font-weight:400;font-size:14px;letter-spacing:2px;color:var(--ink)}
.feature p{position:absolute;top:155px;left:14px;width:183px;font-size:11px;line-height:12px;color:var(--muted)}
.feature .more{position:absolute;top:210px;left:0;width:100%;font-family:"Oswald",sans-serif;font-weight:700;font-size:13px;color:#4a3a30;text-decoration:none}

.section-title{font-family:"Questrial",sans-serif;font-weight:400;font-size:28px;letter-spacing:-1px;color:var(--ink);white-space:nowrap}
.why p{font-size:11px;line-height:14px;color:#333;margin-bottom:14px;width:425px}

.post{left:532px;width:345px;border-bottom:1px dotted #888}
.post .day{position:absolute;left:0;top:0;width:28px;height:28px;border-radius:50%;background:var(--accent);border:2px solid #cfe6f5;color:#fff;font-family:"Oswald",sans-serif;font-weight:500;font-size:15px;text-align:center;line-height:24px}
.post .mon{position:absolute;left:1px;top:33px;font-size:12px;font-weight:700;color:var(--accent)}
.post h4{position:absolute;left:52px;top:0;font-size:11.5px;color:var(--ink)}
.post p{position:absolute;left:53px;top:20px;width:292px;font-size:10px;line-height:12px;color:var(--muted)}
.post .read{position:absolute;left:53px;font-size:10px;font-weight:700;color:var(--brown);text-decoration:none}
.btn-more{left:797px;top:826px;width:78px;height:28px;border-radius:6px;background:var(--tan);border:2px solid #b9a899;color:var(--cream);font-family:"Oswald",sans-serif;font-weight:500;font-size:14px;text-align:center;line-height:24px}

.site-footer{left:0;top:920px;width:923px;height:280px;background:var(--footer);color:var(--white)}
.site-footer h5{position:absolute;top:24px;font-family:"Oswald",sans-serif;font-weight:700;font-size:16px;letter-spacing:.5px;text-transform:uppercase}
.foot-links{position:absolute;top:66px;font-size:11.5px;line-height:13.7px;list-style:none}
.copy{position:absolute;left:32px;top:157px;font-size:11.5px;line-height:13.7px}
.field{position:absolute;left:378px;width:201px;background:var(--cream);border-radius:8px;font-size:11px;color:#6d6d6d;padding:8px 16px}
.submit{position:absolute;left:508px;top:232px;width:70px;height:24px;border-radius:10px;background:var(--accent);color:#fff;font-size:11px;font-weight:700;text-align:center;line-height:24px}
.social{position:absolute;left:675px;top:64px;display:flex;gap:8px}
.social span{width:26px;height:26px;border-radius:50%;background:#d8cdc3;border:2px solid #f0e8e0}
.note{position:absolute;left:675px;top:104px;font-size:10px;line-height:12.5px}
.subscribe-field{position:absolute;left:673px;top:136px;width:175px;height:26px;border-radius:13px;background:var(--cream);font-size:10px;color:#6d6d6d;padding:7px 14px}
.subscribe{position:absolute;left:676px;top:172px;font-size:10px;font-weight:700}
.phone{position:absolute;left:672px;top:204px;display:flex;align-items:center;gap:10px;font-family:"Oswald",sans-serif;font-weight:300;font-size:26px;color:#f4ece4}
</style>
</head>
<body>

<header class="site-header abs">
  <div class="brand abs">BRENWICK IT CONSULTING</div>
  <nav class="main-nav abs">
    <a class="active" href="#">Home</a><a href="#">About us</a><a href="#">Blog</a><a href="#">Shop</a><a href="#">Products and Services</a><a href="#">Contact us</a>
  </nav>
</header>

<div class="hero abs" role="img" aria-label="Hero photograph: technology themed image with digital interface and binary code"></div>

<section class="feature abs" style="left:34px">
  <svg class="cap" width="211" height="92"><polygon points="0,0 211,24 211,70 0,82" fill="var(--ink)"/><polygon points="0,82 211,70 211,80 0,92" fill="var(--tan)"/></svg>
  <div class="badge"><svg width="40" height="34" viewBox="0 0 40 34"><rect x="6" y="4" width="28" height="19" rx="2" fill="none" stroke="#fff" stroke-width="3"/><rect x="2" y="25" width="36" height="4" rx="2" fill="#fff"/></svg></div>
  <h3>PRODUCT 1</h3>
  <p>Lorem ipsum dolor sit amet, consectetur adipisicing elit, sed do eiusmod tempor incididunt ut labore et dolore magna aliqua.</p>
  <a class="more" href="#">READ MORE</a>
</section>
<section class="feature abs" style="left:247px">
  <svg class="cap" width="211" height="92"><polygon points="0,24 211,0 211,82 0,70" fill="var(--ink)"/><polygon points="0,70 211,82 211,92 0,80" fill="var(--tan)"/></svg>
  <div class="badge"><svg width="42" height="36" viewBox="0 0 42 36"><circle cx="14" cy="20" r="9" fill="none" stroke="#fff" stroke-width="5" stroke-dasharray="4 3"/><circle cx="14" cy="20" r="3" fill="#fff"/><circle cx="31" cy="9" r="6" fill="none" stroke="#fff" stroke-width="4" stroke-dasharray="3 2"/><circle cx="31" cy="27" r="5" fill="none" stroke="#fff" stroke-width="4" stroke-dasharray="3 2"/></svg></div>
  <h3>PRODUCT 2</h3>
  <p>Ut enim ad minim veniam, quis nostrud exercitation ullamco laboris nisi ut aliquip ex ea commodo consequat.</p>
  <a class="more" href="#">READ MORE</a>
</section>
<section class="feature abs" style="left:461px">
  <svg class="cap" width="211" height="92"><polygon points="0,0 211,24 211,70 0,82" fill="var(--ink)"/><polygon points="0,82 211,70 211,80 0,92" fill="var(--tan)"/></svg>
  <div class="badge"><svg width="44" height="40" viewBox="0 0 44 40"><circle cx="26" cy="20" r="15" fill="none" stroke="#fff" stroke-width="3"/><circle cx="26" cy="20" r="4" fill="#fff"/><path d="M10 4v22M3 20l7 9 7-9" fill="none" stroke="#fff" stroke-width="4"/></svg></div>
  <h3>SERVICE 1</h3>
  <p>Duis aute irure dolor in reprehend voluptate velit esse cillum dolore eu fugiat nulla pariatur. Excepteur sint occaecat cupidatat non.</p>
  <a class="more" href="#">READ MORE</a>
</section>
<section class="feature abs" style="left:675px">
  <svg class="cap" width="211" height="92"><polygon points="0,24 211,0 211,82 0,70" fill="var(--ink)"/><polygon points="0,70 211,82 211,92 0,80" fill="var(--tan)"/></svg>
  <div class="badge"><svg width="44" height="34" viewBox="0 0 44 34"><circle cx="10" cy="8" r="4" fill="#fff"/><circle cx="22" cy="6" r="4" fill="#fff"/><circle cx="34" cy="8" r="4" fill="#fff"/><rect x="4" y="15" width="36" height="6" fill="#fff"/><rect x="4" y="21" width="5" height="11" fill="#fff"/><rect x="35" y="21" width="5" height="11" fill="#fff"/><rect x="14" y="24" width="16" height="8" fill="#fff"/></svg></div>
  <h3>SERVICE 2</h3>
  <p>Excepteur sint occaecat cupidatat non proident, sunt in culpa qui deserunt mollit anim id est labor esse cillum dolore</p>
  <a class="more" href="#">READ MORE</a>
</section>

<section class="why abs" style="left:37px;top:628px">
  <h2 class="section-title" style="margin-bottom:14px">WHY BRENWICK IT CONSULTING?</h2>
  <p>Sed ut perspiciatis, unde omnis iste natus error sit voluptatem accusantium doloremque laudantium, totam rem aperiam eaque ipsa, quae ab illo inventore veritatis et quasi architecto beatae vitae dicta sunt, explicabo. Nemo enim ipsam voluptatem, quia voluptas sit, aspernatur aut odit aut fugit, sed.</p>
  <p>Voluptatem sequi nesciunt, neque porro quisquam est, qui dolorem ipsum, quia dolor sit amet, consectetur, adipisci[ng] velit, sed quia non numquam [do] eius modi tempora inci[di]dunt, ut labore et dolore magnam aliquam quaerat voluptatem.</p>
</section>

<h2 class="section-title abs" style="left:528px;top:618px">LATEST FROM BLOG</h2>
<article class="post abs" style="top:665px;height:61px">
  <div class="day">27</div><div class="mon">AUG</div>
  <h4>Lorem ipsum dolor sit amet</h4>
  <p>Lorem ipsum dolor sit amet, consectetur adipisicing elit, sed do.</p>
  <a class="read" href="#" style="top:35px">read more +</a>
</article>
<article class="post abs" style="top:740px;height:73px">
  <div class="day">26</div><div class="mon">AUG</div>
  <h4>Sed ut perspiciatis, unde</h4>
  <p>Sed ut perspiciatis, unde omnis istenatus error sit voluptatem accusan</p>
  <a class="read" href="#" style="top:48px">read more +</a>
</article>
<div class="btn-more abs">MORE NEWS</div>

<footer class="site-footer abs">
  <h5 style="left:29px">Site Navigation</h5>
  <ul class="foot-links" style="left:30px"><li>Home</li><li>About us</li><li>Products and Services</li><li>Schedule a demo</li><li>Contact us</li></ul>
  <ul class="foot-links" style="left:188px"><li>Sitemap</li><li>Terms and Conditions</li><li>Privacy Policy</li></ul>
  <div class="copy">© Copyright 2013 Brenwick Software.<br>All Rights Reserved</div>

  <h5 style="left:382px">Email Us</h5>
  <div class="field" style="top:64px;height:27px">full name</div>
  <div class="field" style="top:96px;height:27px">email address</div>
  <div class="field" style="top:126px;height:98px">message</div>
  <div class="submit">submit</div>

  <h5 style="left:677px">Contact Us</h5>
  <div class="social"><span></span><span></span><span></span><span></span><span></span></div>
  <div class="note">subscribe to our monthly newsletter<br>and get the best deals and discounts</div>
  <div class="subscribe-field">enter email address</div>
  <div class="subscribe">➤&nbsp; subscribe now</div>
  <div class="phone"><svg width="26" height="26" viewBox="0 0 26 26"><circle cx="13" cy="13" r="12" fill="none" stroke="#f4ece4" stroke-width="1.5"/><path d="M9 7c-2 1-2 4 0 7s5 6 8 5l1-2-3-2-2 1c-1-1-3-3-3-4l1-2-2-3z" fill="#f4ece4"/></svg>0-12-5550198</div>
</footer>
</body>
</html>
```